Graduation Yearbook Page for a Young Lady

A one page for my daughter's yearbook. She is in 8th grade, which in her school is the year they graduate and go to different highschools. I am looking for a clean and elegant and yet imaginative layout that incorporates "Tessa, Congratulations, We are so very proud of you. Mom, Dad, Grandma, Joan and Harold.
Please feel free as many or as few as 4 of the attached photos. The main photo Tessa Smiling should be in the center.

```html
<!DOCTYPE html>
<html lang="en">
<head>
<meta charset="utf-8">
<title>Tessa, Congratulations</title>
<link rel="stylesheet" href="https://fonts.googleapis.com/css2?family=Great+Vibes&family=Tinos&display=swap">
<style>
  :root {
    --bg-centre: #6b6b6b;
    --bg-edge: #262626;
    --ink: #ffffff;
    --frame: #f7e600;
  }
  html, body {
    margin: 0;
    padding: 0;
    overflow: hidden;
    background: var(--bg-edge);
  }
  .page {
    position: relative;
    width: 848px;
    height: 1200px;
    overflow: hidden;
    background: radial-gradient(ellipse 70% 60% at 50% 52%, var(--bg-centre) 0%, #4a4a4a 55%, var(--bg-edge) 100%);
  }
  .headline {
    position: absolute;
    top: 92px;
    left: 0;
    width: 100%;
    margin: 0;
    text-align: center;
    font-family: "Great Vibes", cursive;
    font-weight: 400;
    font-size: 72px;
    line-height: 1;
    color: var(--ink);
  }
  .photo-eight {
    position: absolute;
    top: 0;
    left: 0;
  }
  .message {
    position: absolute;
    top: 1010px;
    left: 0;
    width: 100%;
    text-align: center;
    font-family: "Tinos", serif;
    color: var(--ink);
  }
  .message-lead {
    margin: 0;
    font-size: 39px;
    line-height: 1.1;
  }
  .message-signoff {
    margin: 6px 0 0;
    font-size: 29px;
    line-height: 1.3;
  }
</style>
</head>
<body>
<main class="page">
  <h1 class="headline">Tessa, Congratulations</h1>

  <svg class="photo-eight" width="848" height="1200" viewBox="0 0 848 1200">
    <defs>
      <clipPath id="eight-shape">
        <path d="M236,226 H653 Q743,226 743,316 V500 Q743,580 660,588 L622,592 L666,600 Q746,612 746,700 V869 Q746,969 646,969 H242 Q142,969 142,869 V700 Q142,612 222,600 L253,594 L226,588 Q146,578 146,500 V316 Q146,226 236,226 Z"/>
      </clipPath>
      <linearGradient id="tone-toddler" x1="0" y1="0" x2="1" y2="1">
        <stop offset="0" stop-color="#6e3a2a"/>
        <stop offset="0.5" stop-color="#c9997e"/>
        <stop offset="1" stop-color="#8a5a48"/>
      </linearGradient>
      <linearGradient id="tone-young" x1="0" y1="0" x2="1" y2="1">
        <stop offset="0" stop-color="#5a4536"/>
        <stop offset="0.5" stop-color="#d7b7a2"/>
        <stop offset="1" stop-color="#e9e6e4"/>
      </linearGradient>
      <linearGradient id="tone-summer" x1="0" y1="0" x2="1" y2="1">
        <stop offset="0" stop-color="#f1efe9"/>
        <stop offset="0.6" stop-color="#b9a48e"/>
        <stop offset="1" stop-color="#6b5440"/>
      </linearGradient>
      <linearGradient id="tone-city" x1="0" y1="0" x2="1" y2="1">
        <stop offset="0" stop-color="#b77a52"/>
        <stop offset="0.5" stop-color="#9c9c9c"/>
        <stop offset="1" stop-color="#1f2a26"/>
      </linearGradient>
      <linearGradient id="tone-portrait" x1="0" y1="0" x2="0" y2="1">
        <stop offset="0" stop-color="#2b1a12"/>
        <stop offset="0.5" stop-color="#c88a5c"/>
        <stop offset="1" stop-color="#3a2418"/>
      </linearGradient>
      <linearGradient id="tone-harbour" x1="0" y1="0" x2="0" y2="1">
        <stop offset="0" stop-color="#2f6fd0"/>
        <stop offset="0.55" stop-color="#d98aa6"/>
        <stop offset="1" stop-color="#d8d4cc"/>
      </linearGradient>
    </defs>

    <g clip-path="url(#eight-shape)">
      <rect x="140" y="220" width="285" height="378" fill="url(#tone-toddler)" role="img" aria-label="Photo of Tessa as a toddler in a red hat"/>
      <rect x="425" y="220" width="325" height="378" fill="url(#tone-young)" role="img" aria-label="Photo of Tessa as a young girl smiling"/>
      <rect x="140" y="598" width="285" height="375" fill="url(#tone-summer)" role="img" aria-label="Photo of Tessa in sunglasses on a summer day"/>
      <rect x="425" y="598" width="325" height="375" fill="url(#tone-city)" role="img" aria-label="Photo of Tessa in a dark hoodie in the city"/>
    </g>
    <path d="M236,226 H653 Q743,226 743,316 V500 Q743,580 660,588 L622,592 L666,600 Q746,612 746,700 V869 Q746,969 646,969 H242 Q142,969 142,869 V700 Q142,612 222,600 L253,594 L226,588 Q146,578 146,500 V316 Q146,226 236,226 Z"
          fill="none" stroke="var(--frame)" stroke-width="4.5" stroke-linejoin="round"/>

    <rect x="357" y="350" width="168" height="174" rx="20" fill="url(#tone-portrait)" stroke="var(--frame)" stroke-width="4.5" role="img" aria-label="Main photo of Tessa smiling"/>
    <rect x="359" y="645" width="168" height="203" rx="20" fill="url(#tone-harbour)" stroke="var(--frame)" stroke-width="4.5" role="img" aria-label="Photo of Tessa by the harbour under a blue sky"/>
  </svg>

  <section class="message">
    <p class="message-lead">We are so very proud of you.</p>
    <p class="message-signoff">Mom, Dad, Grandma,<br>Joan and Harold.</p>
  </section>
</main>
</body>
</html>
```